Consulting and solution company website in MS Webmatrix

We need a website for a new healthcare consulting company that provides management consulting and innovative solutions for patient safety. We offer 1 product with plans to add 2 more and we offer consulting services to implement, train, select, improve, the patient safety programs. We provide services to both patient safety organizations and health care provider's (mainly hospitals and health systems). We want the website to convey an innovative, hard-working, energetic company bringing new ideas to healthcare. We do not want a bunch of stock pictures of people looking smart and busy in suits and doctor/nurse garb. T We love adventure, jumping ino the middle of a problem, and are thrilled to be a small and disruptive startup. The problems are very serious and complex issues so we have to tasteful in the design but not typical and boring. he site must be in .net and be device responsive. We will manage the site in MS Webmatrix and if db is used it must be MS SQL. Many of the new and fresh templates I have seen are great. We just can't seem to pull it all together when we start "tweaking" the design. We have modified a standard template to demonstrate where we are headed, but need a higher quality than we are able to build.

My current test site is at http://sandbox.brightquillsolutions.example/

Sites I like
http://www.vormitsoftware.example/
http://ledgerly.zandaro.example/
https://www.taskharbor.example/
http://www.dealmoor.example/
http://www.wbkta.example/

Companies in my market:
www.Mvoyields.example
www.Bramblegrp.example
www.Tksolutions.example
www.Velmarix.example

Target Market(s)

Healthcare providers like chief executives of hospitals, Nursing administrators, Patient Safety Professionals (www.gdkw.example) and physicians/Chief Medical Officers.

Industry/Entity Type

Management Consulting

Font styles to use
Sans Serif

Requirements
Must have
• Must have a put together feel graphically, clean, simple
Must be able to own all design materials.
Must be able to update content with some homework by us
Must have a picture slider
Must be based on .net/mssql.
Nice to have
• Blog page behind a registration process
Register and pull down whitepaper materials
Responsive design

```html
<!DOCTYPE html>
<html lang="en">
<head>
<meta charset="utf-8">
<title>BrightQuill Solutions</title>
<link rel="stylesheet" href="https://fonts.googleapis.com/css2?family=Open+Sans:wght@300;400;600;700&display=swap">
<style>
:root{
  --brand:#0f4a12;
  --brand-dark:#0a2e0c;
  --footer:#0b2a0d;
  --text:#555;
  --muted:#999;
  --line:#ececec;
  --orange:#efa731;
  --orange-dark:#d99a30;
  --green:#5db08c;
  --green-dark:#54a07f;
  --red:#e85c5f;
  --red-dark:#d45356;
  --panel:#f6f6f6;
}
*{box-sizing:border-box;margin:0;padding:0}
html,body{width:910px;height:1200px;overflow:hidden}
body{font-family:'Open Sans',sans-serif;background:#fff;color:var(--text);position:relative}
.wrap{position:absolute;left:130px;width:651px}

.site-header{position:absolute;top:0;left:0;width:910px;height:86px;border-bottom:1px solid var(--line)}
.logo{position:absolute;left:130px;top:26px;display:flex;align-items:center;gap:8px}
.logo-mark{width:24px;height:24px;background:var(--brand)}
.logo-name{font-size:28px;font-weight:700;color:var(--brand);letter-spacing:-.5px}
.contact{position:absolute;right:129px;top:38px;display:flex;gap:18px;font-size:9.5px;color:var(--muted)}
.contact span{display:flex;align-items:center;gap:8px}
.ico-dot{width:18px;height:18px;border-radius:50%;background:#f2f2f2;display:flex;align-items:center;justify-content:center}

.main-nav{position:absolute;top:86px;left:0;width:910px;height:40px;border-bottom:1px solid var(--line)}
.main-nav ul{list-style:none;display:flex;position:absolute;left:130px;width:651px;height:40px}
.main-nav li{flex:1;display:flex;align-items:center;justify-content:center;gap:8px;font-size:10.5px;color:#777;border-right:1px solid #f1f1f1}
.main-nav li:last-child{border-right:none}

.hero{position:absolute;top:126px;left:0;width:910px;height:356px;
  background:radial-gradient(circle at 50% 8%,#fff6c8 0,#e9dca0 12%,transparent 35%),
  linear-gradient(180deg,#a9aeb0 0%,#c9cfd0 22%,#8a9a7e 45%,#5d7a45 62%,#6f6a50 82%,#a39a82 100%)}
.slide-arrow{position:absolute;top:170px;width:26px;height:26px;border-radius:50%;background:rgba(40,40,40,.75);display:flex;align-items:center;justify-content:center}

.features{position:absolute;top:509px;left:130px;display:flex;gap:18px}
.feature{width:205px;height:192px;color:#fff;text-align:center;position:relative}
.feature .icon{width:60px;height:60px;border-radius:50%;margin:14px auto 0;display:flex;align-items:center;justify-content:center;background:rgba(0,0,0,.04)}
.feature h3{font-size:12.5px;font-weight:600;margin-top:10px}
.feature p{font-size:8.4px;line-height:14.4px;margin:9px 14px 0;opacity:.95}
.feature .toggle{position:absolute;bottom:0;left:0;right:0;height:31px;display:flex;align-items:center;justify-content:center}
.f-orange{background:var(--orange)}.f-orange .toggle{background:var(--orange-dark)}
.f-green{background:var(--green)}.f-green .toggle{background:var(--green-dark)}
.f-red{background:var(--red)}.f-red .toggle{background:var(--red-dark)}

.welcome{position:absolute;top:726px;left:130px;width:372px;height:206px;background:#fcfcfc;border:1px solid #f3f3f3}
.welcome h2{font-size:16px;font-weight:400;color:#444;padding:13px 18px 10px;border-bottom:1px solid #f0f0f0}
.welcome p{font-size:8.2px;line-height:15px;color:var(--muted);margin:12px 18px 0}
.welcome p+p{margin-top:7px}
.welcome .more{display:block;font-size:8.5px;color:#555;margin:9px 18px 0}

.services{position:absolute;top:726px;left:520px;width:261px}
.service{position:relative;height:104px;border-bottom:1px solid #f1f1f1}
.service .badge{position:absolute;left:1px;top:16px;width:74px;height:74px;border-radius:50%;border:4px solid #f4f4f4;display:flex;align-items:center;justify-content:center;background:#fff}
.service h4{position:absolute;left:94px;top:18px;font-size:12px;font-weight:400;color:#888}
.service p{position:absolute;left:94px;top:42px;right:0;font-size:8px;line-height:14.4px;color:var(--muted);text-align:justify}

.help{position:absolute;top:958px;left:130px;width:651px;height:154px;background:var(--panel)}
.help h2{text-align:center;font-size:15px;font-weight:400;color:#444;margin-top:16px}
.field{position:absolute;background:#fff;border:1px solid #eee;font-size:8.2px;color:#aaa;padding:0 13px;display:flex;align-items:center;height:31px;width:180px}
.field.area{align-items:flex-start;padding-top:10px;height:43px;width:382px}
.submit{position:absolute;left:440px;top:90px;width:178px;height:41px;background:linear-gradient(#0d4410,#062807);color:#fff;font-size:15px;display:flex;align-items:center;justify-content:center;border-radius:2px}

.site-footer{position:absolute;top:1140px;left:0;width:910px;height:60px;background:var(--footer);font-size:8px;color:#aab6aa}
.site-footer .copy{position:absolute;left:131px;top:25px}
.social{position:absolute;left:435px;top:19px;display:flex;gap:4px}
.social span{width:18px;height:18px;border-radius:50%;border:1px solid #8a9a8a}
.foot-nav{position:absolute;right:129px;top:25px}
</style>
</head>
<body>

<header class="site-header">
  <div class="logo"><span class="logo-mark"></span><span class="logo-name">BrightQuill</span></div>
  <div class="contact">
    <span><span class="ico-dot"><svg width="8" height="8" viewBox="0 0 10 10"><path d="M2 1h2l1 2-1 1a6 6 0 0 0 2 2l1-1 2 1v2c-4 1-8-3-7-7z" fill="#888"/></svg></span>Call : 555.014.2290</span>
    <span><span class="ico-dot"><svg width="9" height="7" viewBox="0 0 10 8"><rect x=".5" y=".5" width="9" height="7" fill="none" stroke="#888"/><path d="M.5 .5 5 4.5 9.5 .5" fill="none" stroke="#888"/></svg></span>info@brightquillsolutions.example</span>
  </div>
</header>

<nav class="main-nav">
  <ul>
    <li>Home</li><li>About</li><li>Solutions</li><li>Services</li><li>Contact Us</li>
    <li><span class="ico-dot"><svg width="8" height="8" viewBox="0 0 10 10"><circle cx="5" cy="3" r="2.2" fill="#888"/><path d="M1 10a4 4 0 0 1 8 0z" fill="#888"/></svg></span>Register</li>
    <li><span class="ico-dot"><svg width="8" height="8" viewBox="0 0 10 10"><rect x="1.5" y="4.5" width="7" height="5" fill="#888"/><path d="M3 4.5V3a2 2 0 0 1 4 0v1.5" fill="none" stroke="#888" stroke-width="1.2"/></svg></span>Login</li>
  </ul>
</nav>

<section class="hero" role="img" aria-label="Photo slide: hiker with raised arms on a mountain ridge under a bright cloudy sky">
  <div class="slide-arrow" style="left:33px"><svg width="10" height="10" viewBox="0 0 10 10"><path d="M7 1 3 5l4 4" fill="none" stroke="#fff" stroke-width="1.6"/></svg></div>
  <div class="slide-arrow" style="right:31px"><svg width="10" height="10" viewBox="0 0 10 10"><path d="M3 1l4 4-4 4" fill="none" stroke="#fff" stroke-width="1.6"/></svg></div>
</section>

<section class="features">
  <article class="feature f-orange">
    <div class="icon"><svg width="48" height="48" viewBox="0 0 48 48"><g fill="#fff"><circle cx="24" cy="24" r="17"/><g stroke="#fff" stroke-width="7"><path d="M24 2v44M2 24h44M8 8l32 32M40 8 8 40"/></g></g><circle cx="24" cy="24" r="11" fill="var(--orange)"/><circle cx="24" cy="24" r="7" fill="#fff"/></svg></div>
    <h3>Needs Assessment</h3>
    <p>Our proprietary methodology evaluates your current program systematically comparing to industry standards and national</p>
    <div class="toggle"><svg width="10" height="6" viewBox="0 0 10 6"><path d="M1 1l4 4 4-4" fill="none" stroke="#fff" stroke-width="1.5"/></svg></div>
  </article>
  <article class="feature f-green">
    <div class="icon"><svg width="40" height="40" viewBox="0 0 40 40"><g fill="#fff"><path d="M6 28l6-3v12H6z"/><path d="M15 23l6-3v17h-6z"/><path d="M24 17l6-4v24h-6z"/><path d="M33 6l4-2v33h-4z"/></g></svg></div>
    <h3>Process Analysis</h3>
    <p>Our proprietary methodology evaluates your current program systematically comparing to industry standards and national</p>
    <div class="toggle"><svg width="10" height="6" viewBox="0 0 10 6"><path d="M1 1l4 4 4-4" fill="none" stroke="#fff" stroke-width="1.5"/></svg></div>
  </article>
  <article class="feature f-red">
    <div class="icon"><svg width="44" height="44" viewBox="0 0 44 44"><g fill="none" stroke="#fff" stroke-width="3.5"><circle cx="20" cy="20" r="16"/><circle cx="20" cy="20" r="8"/></g><path d="M20 20l20 7-8 3-3 8z" fill="#fff" stroke="var(--red)" stroke-width="1.5"/></svg></div>
    <h3>Optimization</h3>
    <p>Our proprietary methodology evaluates your current program systematically comparing to industry standards and national</p>
    <div class="toggle"><svg width="10" height="6" viewBox="0 0 10 6"><path d="M1 1l4 4 4-4" fill="none" stroke="#fff" stroke-width="1.5"/></svg></div>
  </article>
</section>

<section class="welcome">
  <h2>Welcome To BrightQuill</h2>
  <p>Praesent vestibulum molestie lacus. Aenean nonummy hendrerit mauris. Phasellus porta. Fusce suscipit varius mi. Cum sociis natoque penatibus et ma dis parturient montes, nascetur ridiculus mus. Nulla dui. Fusce male.</p>
  <p>Morbi nunc odio, gravida at, cursus nec, luctus a, lorem. Maecenas tristique orci ac sem. Duis ultricies pharetra magna. Donec accumsan malesuada orci. Donec sit amet eros. Lorem ipsum dolor sit amet, consectetuer adipiscing elit. Mauris fermentum dictum magna.</p>
  <a class="more">Read More +</a>
</section>

<section class="services">
  <div class="service">
    <div class="badge"><svg width="30" height="34" viewBox="0 0 30 34"><g fill="#222"><rect x="14" y="2" width="2" height="30"/><circle cx="15" cy="4" r="2.5"/><path d="M14 9C9 5 3 6 0 10c5-1 9 0 14 3z"/><path d="M16 9c5-4 11-3 14 1-5-1-9 0-14 3z"/><path d="M10 14c4 2 10 3 10 6s-6 4-6 7 4 3 6 4" fill="none" stroke="#222" stroke-width="1.8"/></g></svg></div>
    <h4>Health Analytics</h4>
    <p>Nulla ornare, nulla et egestas hendrerit, ipsum dui vulputate dolor, et ornare orci erat eleifend pede. Fusce eros</p>
  </div>
  <div class="service">
    <div class="badge"><svg width="26" height="30" viewBox="0 0 26 30"><circle cx="13" cy="8" r="6.5" fill="#222"/><path d="M1 30a12 12 0 0 1 24 0z" fill="#222"/><path d="M13 20v7M9.5 23.5h7" stroke="#fff" stroke-width="1.8"/></svg></div>
    <h4>Healthcare Consulting</h4>
    <p>Nulla ornare, nulla et egestas hendrerit, ipsum dui vulputate dolor, et ornare orci erat eleifend pede. Fusce eros</p>
  </div>
</section>

<section class="help">
  <h2>How can we help?</h2>
  <div class="field" style="left:34px;top:48px">Full Name</div>
  <div class="field" style="left:236px;top:48px">Your email:</div>
  <div class="field" style="left:438px;top:48px">Phone</div>
  <div class="field area" style="left:34px;top:90px">Questions/Comments:</div>
  <div class="submit">Submit</div>
</section>

<footer class="site-footer">
  <div class="copy">©2013 - 2014 &nbsp;BRIGHTQUILL SOLUTIONS LLC, ALL RIGHTS RESERVED.</div>
  <div class="social"><span></span><span></span><span></span><span></span><span></span></div>
  <div class="foot-nav">ABOUT US &nbsp;| &nbsp;SERVICES | &nbsp;SOLUTIONS &nbsp;| &nbsp;CONTACT</div>
</footer>

</body>
</html>
```